New business card for UK roofing company

We are Penwick Roofing and we need a business card design for our staff.

We offer the following services:

- New roofs
- General roof repairs
- Drone surveys
- Single ply roofing
- Steel cladding
- Asbestos removal
- Electronic leak detection

I have attached our logo. I have also attached example branding printed to our vans. The business card should fit in with the style of our branding.

The business card should have the following information;

Address:
Unit 17c Marlow Dene Farm
Marlow Dene Lane
Fenbury
RX4 9QD

Telephone: 020 7946 0312
24 Hour: 0800 471 9062

Email: tom@penwickroofing.com
Mobile: 07700900418
Name: Tom Harley
Website: www.penwickroofing.com

The business card will be printed in Spot UV, see here: https://www.printvane.com/business-cards/spot-uv/

If you need anymore info, please let me know,

```html
<!DOCTYPE html>
<html lang="en">
<head>
<meta charset="utf-8">
<title>Penwick Roofing business card</title>
<link href="https://fonts.googleapis.com/css2?family=Montserrat:wght@400;500;700&display=swap" rel="stylesheet">
<style>
  :root {
    --navy: #0d3b73;
    --navy-deep: #0a2e5c;
    --blue: #1a5fae;
    --cyan: #1ab0e6;
    --ink: #4a4f57;
    --paper: #ffffff;
    --backdrop: #b1b1ad;
  }
  * { box-sizing: border-box; margin: 0; padding: 0; }
  html, body { width: 1200px; height: 801px; overflow: hidden; }
  body {
    background: var(--backdrop);
    font-family: "Montserrat", sans-serif;
    position: relative;
  }
  .card {
    position: absolute;
    top: 232px;
    width: 520px;
    height: 336px;
    border-bottom: 6px solid var(--cyan);
    box-shadow: 0 14px 28px rgba(0,0,0,.25);
  }
  .card--front { left: 60px; background: var(--paper); }
  .card--back { left: 620px; background: var(--navy); overflow: hidden; }

  /* front */
  .identity { position: absolute; left: 32px; bottom: 196px; }
  .identity__name { font-weight: 700; font-size: 30px; color: var(--navy); letter-spacing: -.5px; line-height: 1; }
  .identity__role { font-size: 13px; color: var(--ink); letter-spacing: 1px; margin-top: 4px; }
  .divider { position: absolute; left: 32px; right: 32px; top: 146px; height: 1px; background: var(--navy); }
  .contact { list-style: none; font-size: 12.5px; color: var(--ink); line-height: 19px; }
  .contact li { display: flex; align-items: center; gap: 7px; }
  .contact svg { width: 10px; height: 10px; flex: none; fill: none; stroke: var(--navy); stroke-width: 1.6; }
  .contact--personal { position: absolute; left: 32px; top: 160px; }
  .contact--office { position: absolute; left: 280px; top: 22px; }
  .address { position: absolute; left: 297px; top: 84px; font-size: 12.5px; color: var(--ink); line-height: 17px; font-style: normal; }
  .address::before { content: ""; position: absolute; left: -17px; top: 7px; width: 9px; height: 1.5px; background: var(--navy); }
  .services { position: absolute; left: 280px; top: 160px; list-style: none; font-size: 12.5px; color: var(--ink); line-height: 17.5px; }
  .services li { display: flex; align-items: center; gap: 8px; }
  .services li::before { content: ""; width: 9px; height: 9px; border-radius: 50%; background: var(--cyan); flex: none; }

  /* back */
  .pattern {
    position: absolute; inset: 0;
    background: radial-gradient(ellipse at 15% 90%, var(--blue) 0%, var(--navy) 55%, var(--navy-deep) 100%);
  }
  .brand {
    position: absolute; right: 46px; bottom: 68px;
    display: flex; align-items: center; gap: 10px;
  }
  .brand__dot { width: 30px; height: 30px; border-radius: 50%; background: var(--cyan); }
  .brand__name { font-weight: 700; font-size: 30px; color: var(--paper); letter-spacing: -.8px; }
</style>
</head>
<body>
  <section class="card card--front" aria-label="Business card front">
    <div class="identity">
      <h1 class="identity__name">TOM HARLEY</h1>
      <p class="identity__role">DIRECTOR</p>
    </div>

    <ul class="contact contact--office">
      <li><svg viewBox="0 0 10 10"><path d="M1 4c0-2 8-2 8 0M2 4l1 1M8 4 7 5M2 5h6v3H2z"/></svg>020 7946 0312</li>
      <li><svg viewBox="0 0 10 10"><path d="M3 1 1.5 2.5c0 3 3 6 6 6L9 7 7 5.5 6 6.5C5 6 4 5 3.5 4l1-1z"/></svg>0800 471 9062 (24 Hour)</li>
      <li><svg viewBox="0 0 10 10"><circle cx="5" cy="5" r="4"/><path d="M1 5h8M5 1c-2 2-2 6 0 8M5 1c2 2 2 6 0 8"/></svg>www.penwickroofing.com</li>
    </ul>
    <address class="address">
      Unit 17c Marlow Dene Farm<br>
      Marlow Dene Lane Fenbury<br>
      RX4 9QD
    </address>

    <div class="divider"></div>

    <ul class="contact contact--personal">
      <li><svg viewBox="0 0 10 10"><rect x="2.5" y="1" width="5" height="8" rx=".8"/></svg>07700900418</li>
      <li><svg viewBox="0 0 10 10"><rect x="1" y="2" width="8" height="6"/><path d="m1 2 4 3.5L9 2"/></svg>tom@penwickroofing.com</li>
    </ul>

    <ul class="services">
      <li>New roofs</li>
      <li>General roof repairs</li>
      <li>Drone surveys</li>
      <li>Single ply roofing</li>
      <li>Steel cladding</li>
      <li>Asbestos removal</li>
      <li>Electronic leak detection</li>
    </ul>
  </section>

  <section class="card card--back" aria-label="Business card back">
    <div class="pattern" role="img" aria-label="Repeating spot UV brand emblem pattern on navy"></div>
    <div class="brand">
      <span class="brand__dot"></span>
      <span class="brand__name">penwickroofing</span>
    </div>
  </section>
</body>
</html>
```